Plakat-Design für Werbetafel-Design für Fussballplatz
Zielgruppe
IT Consulting Dienstleistungen für Internationale Kunden
Aufgabenstellung
Werbetafel-Design für Fussballplatz. (Logo in groß + Slogan 'THE IT CONSULTANS')
Format: 3,0 x 0,75 m
Druckdatenvorabe anbei.

```html
<!DOCTYPE html>
<html lang="en">
<head>
<meta charset="utf-8">
<title>VELNOTEC – Stadium Board</title>
<link rel="stylesheet" href="https://fonts.googleapis.com/css2?family=Raleway:wght@400;500&family=Open+Sans:wght@700&display=swap">
<style>
  :root {
    --backdrop: #252b2e;
    --board: #ffffff;
    --brand-blue: #2e82bf;
    --brand-green: #6c9c33;
    --ink: #1e1e1e;
    --band-text: #ffffff;
    --pattern-tint: rgba(255, 255, 255, 0.55);
  }
  * { margin: 0; padding: 0; box-sizing: border-box; }
  html, body {
    width: 1200px;
    height: 774px;
    overflow: hidden;
    background: var(--backdrop);
  }
  .stage {
    position: relative;
    width: 1200px;
    height: 774px;
  }
  .board {
    position: absolute;
    left: 58px;
    width: 1084px;
    height: 271px;
    background: var(--board);
  }
  .board--blue { top: 58px; --band: var(--brand-blue); }
  .board--green { top: 445px; --band: var(--brand-green); }

  .brand-mark {
    position: absolute;
    left: 190px;
    top: 40px;
    width: 118px;
    height: 118px;
    background: var(--brand-blue);
  }
  .brand-name {
    position: absolute;
    left: 442px;
    top: 40px;
    font-family: "Raleway", sans-serif;
    font-weight: 400;
    font-size: 98px;
    line-height: 1;
    letter-spacing: 2px;
    color: var(--ink);
  }
  .brand-tagline {
    position: absolute;
    right: 158px;
    top: 143px;
    font-family: "Raleway", sans-serif;
    font-weight: 500;
    font-size: 38px;
    line-height: 1;
    color: var(--brand-blue);
  }
  .band {
    position: absolute;
    left: 0;
    bottom: 0;
    width: 100%;
    height: 73px;
    background: var(--band);
  }
  .band-pattern {
    position: absolute;
    top: 0;
    height: 73px;
    width: 173px;
    background: linear-gradient(135deg, var(--pattern-tint), rgba(255,255,255,0.25));
  }
  .band-pattern--left { left: 45px; }
  .band-pattern--right { left: 886px; }
  .slogan {
    position: absolute;
    left: 0;
    width: 100%;
    top: 12px;
    text-align: center;
    font-family: "Open Sans", sans-serif;
    font-weight: 700;
    font-size: 50px;
    line-height: 1;
    letter-spacing: 1px;
    color: var(--band-text);
  }
</style>
</head>
<body>
  <main class="stage">
    <section class="board board--blue">
      <div class="brand-mark"></div>
      <div class="brand-name">VELNOTEC</div>
      <div class="brand-tagline">IT Consulting</div>
      <div class="band">
        <div class="band-pattern band-pattern--left" role="img" aria-label="Scattered white pixel squares decoration"></div>
        <p class="slogan">THE IT CONSULTANS</p>
        <div class="band-pattern band-pattern--right" role="img" aria-label="Scattered white pixel squares decoration"></div>
      </div>
    </section>

    <section class="board board--green">
      <div class="brand-mark"></div>
      <div class="brand-name">VELNOTEC</div>
      <div class="brand-tagline">IT Consulting</div>
      <div class="band">
        <div class="band-pattern band-pattern--left" role="img" aria-label="Scattered white pixel squares decoration"></div>
        <p class="slogan">THE IT CONSULTANS</p>
        <div class="band-pattern band-pattern--right" role="img" aria-label="Scattered white pixel squares decoration"></div>
      </div>
    </section>
  </main>
</body>
</html>
```